BenQoral Medical

We are a medical supplier company we sell machines and equipment to all medical sectors in Iraq. Our services include not only the installation of these machines and equipment but also we provide support after installation and we train the staff to use these machines/equipment
We need a website that will make us stand out from our competitors, something professional and catchy
Starting from the home page, before showing the home page we want the loading screen to have our logo animated in a nice way
Then we can proceed to creating the other pages which are
Projects
Services
Training
About
and Contact us
Attached below is our logo and the color blue that we hope to use in the theme of the website
**** In the home page we want to focus on our partners and services****

Target Market(s)

Medical Sector

Industry/Entity Type

Medical

Coding

Coded - Design and coding required

Number of Pages Required

5+ page

Colors
0054AA
0677BA
7BADD7
CADEEF
E8F1F8

Requirements
Must have
• Animation in loading screen or animation in home page
Nice to have
• Some sort of animation for our partners

```html
<!DOCTYPE html>
<html lang="en">
<head>
<meta charset="utf-8">
<title>BenQoral Medical</title>
<link href="https://fonts.googleapis.com/css2?family=Montserrat:wght@500;600;700&family=Lato:wght@400;700&display=swap" rel="stylesheet">
<style>
:root{
  --navy:#1f2060;
  --navy-deep:#1d1c5c;
  --blue:#1e9bd7;
  --blue-label:#2b8fd0;
  --ink:#2a2a2a;
  --muted:#555a66;
  --light:#f3f3f4;
  --line:#d4d6dc;
}
*{margin:0;padding:0;box-sizing:border-box}
html,body{width:1200px;height:4354px;overflow:hidden;background:#fff}
body{font-family:'Lato',sans-serif;color:var(--ink);position:relative}
.abs{position:absolute}
section,header,footer{position:absolute;left:0;width:1200px}
.label{font-family:'Lato',sans-serif;font-size:20px;color:var(--blue-label);letter-spacing:.3px}
.heading{font-family:'Montserrat',sans-serif;font-weight:700;color:var(--navy);font-size:40px}
.center{left:0;width:1200px;text-align:center}
.body-text{font-size:17px;line-height:27px;color:var(--muted)}
.btn{position:absolute;background:var(--blue);color:#fff;font-family:'Lato',sans-serif;font-weight:700;font-size:18px;border-radius:31px;display:flex;align-items:center;justify-content:center;letter-spacing:.3px}
.photo{position:absolute}

/* header */
.site-header{top:0;height:107px;background:#fff}
.brand{left:110px;top:22px;display:flex;align-items:center;gap:14px}
.brand-mark{width:46px;height:46px;background:var(--blue)}
.brand-name{font-family:'Montserrat',sans-serif;font-weight:700;font-size:30px;color:var(--navy);line-height:1}
.brand-sub{font-family:'Montserrat',sans-serif;font-weight:600;font-size:10px;letter-spacing:2.4px;color:var(--navy);margin-top:4px}
.topbar{top:19px;right:110px;font-size:17px;font-weight:700;color:var(--ink);display:flex;gap:22px;align-items:center}
.topbar span{display:flex;align-items:center;gap:6px}
.nav{top:64px;left:532px;font-family:'Lato',sans-serif;font-weight:700;font-size:18px;color:var(--ink)}
.nav a{position:absolute;white-space:nowrap;text-decoration:none;color:inherit}

/* hero */
.hero{top:107px;height:600px}
.hero .photo{left:0;top:0;width:1200px;height:600px;background:linear-gradient(90deg,#16324f 0%,#2a5274 35%,#6f8aa0 60%,#c9d3db 78%,#8fa1b1 100%)}
.hero-kicker{left:108px;top:112px;font-size:20px;color:#3ea6e6}
.hero-title{left:106px;top:150px;font-family:'Montserrat',sans-serif;font-weight:700;font-size:64px;color:#fff;line-height:1}
.hero-text{left:110px;top:254px;width:460px;font-size:21px;line-height:34px;color:#fff}

/* about */
.about{top:707px;height:557px;background:#fff}

/* projects */
.projects{top:1264px;height:1035px;background:linear-gradient(180deg,#dbe9f3 0%,#eef3f7 45%,#f6f6f7 100%)}
.year{position:absolute;top:430px;width:120px;text-align:center;font-size:22px;color:var(--ink)}
.month{position:absolute;left:108px;font-size:20px;color:var(--ink)}
.month-text{position:absolute;left:108px;width:500px;font-size:16px;line-height:25px;color:var(--muted)}

/* services */
.services{top:2299px;height:689px;background:#fff}
.card{position:absolute;top:224px;height:357px}
.card-title{position:absolute;left:0;right:0;bottom:24px;text-align:center;color:#fff;font-size:21px;font-weight:700}

/* training */
.training{top:2988px;height:548px;background:var(--light)}

/* partners */
.partners{top:3536px;height:407px;background:#fff}
.partner{position:absolute;top:226px;width:182px;height:93px;border:1px solid var(--line);background:#fff;display:flex;align-items:center;justify-content:center}
.partner.active{border-color:#7bbde2}
.partner i{display:block;width:44px;height:44px;background:#c3c6cd}

/* footer */
.site-footer{top:3943px;height:411px;background:var(--navy-deep);color:#fff}
.footer-title{font-size:18px;font-weight:700}
.footer-links{font-size:16px;line-height:29px}
.footer-contact{font-size:16px;line-height:24px}
.social{position:absolute;top:338px;width:44px;height:44px;border:2px solid #5a8ad8;border-radius:50%}
</style>
</head>
<body>

<header class="site-header">
  <div class="abs brand">
    <div class="brand-mark"></div>
    <div>
      <div class="brand-name">BenQoral Medical</div>
      <div class="brand-sub">FOR MEDICAL APPLIANCES</div>
    </div>
  </div>
  <div class="abs topbar">
    <span><svg width="16" height="16" viewBox="0 0 24 24"><path fill="#1e9bd7" d="M6.6 10.8a15 15 0 0 0 6.6 6.6l2.2-2.2c.3-.3.7-.4 1-.2 1.1.4 2.3.6 3.6.6.6 0 1 .4 1 1V20c0 .6-.4 1-1 1A17 17 0 0 1 3 4c0-.6.4-1 1-1h3.5c.6 0 1 .4 1 1 0 1.3.2 2.5.6 3.6.1.3 0 .7-.2 1z"/></svg>Call: 1 800 555 0142</span>
    <span><svg width="14" height="16" viewBox="0 0 14 16"><circle cx="7" cy="4" r="3.5" fill="#1e9bd7"/><path d="M0 16c0-4.5 3-7 7-7s7 2.5 7 7z" fill="#1e9bd7"/></svg>Login</span>
  </div>
  <nav class="abs nav">
    <a style="left:0">Projects</a>
    <a style="left:100px">Services</a>
    <a style="left:207px">Training</a>
    <a style="left:313px">About</a>
    <a style="left:411px">Contact us</a>
    <svg class="abs" style="left:540px;top:3px" width="18" height="18" viewBox="0 0 18 18"><circle cx="7.5" cy="7.5" r="5.5" fill="none" stroke="#222" stroke-width="2.5"/><path d="M11.5 11.5l5 5" stroke="#222" stroke-width="2.8"/></svg>
  </nav>
</header>

<section class="hero">
  <div class="photo" role="img" aria-label="Patient vital signs monitor on a hospital trolley"></div>
  <div class="abs hero-kicker">FOR MEDICAL APPLIANCES</div>
  <div class="abs hero-title">BenQoral Medical</div>
  <div class="abs hero-text">We are a medical supplier company we sell machines and equipment to all medical sectors in Iraq.</div>
  <div class="btn" style="left:110px;top:400px;width:191px;height:60px">GET MORE INFO</div>
</section>

<section class="about">
  <div class="photo" role="img" aria-label="Radiotherapy and imaging machines in a treatment room" style="left:112px;top:103px;width:488px;height:373px;background:linear-gradient(135deg,#eef0f2 0%,#c9ced3 40%,#8e9aa6 60%,#dfe3e6 100%)"></div>
  <div class="abs label" style="left:652px;top:84px">ABOUT</div>
  <div class="abs heading" style="left:652px;top:122px">Welcome to BenQoral</div>
  <div class="abs body-text" style="left:652px;top:199px;width:440px">Lorem ipsum dolor sit amet, consectetur adipiscing elit, sed do eiusmod tempor incididunt ut labore et dolore magna aliqua. Ut enim ad minim veniam, quis nostrud exercitation ullamco laboris nisi ut aliquip ex ea commo do consequa e dolor in reprehend.</div>
  <div class="btn" style="left:652px;top:375px;width:158px;height:62px">READ MORE</div>
</section>

<section class="projects">
  <div class="abs label center" style="top:66px">PROJECTS</div>
  <div class="abs heading center" style="top:104px">Recent Projects</div>

  <svg class="abs" style="left:0;top:200px" width="1200" height="240" viewBox="0 0 1200 240">
    <line x1="84" y1="121" x2="1114" y2="121" stroke="var(--navy)" stroke-width="3"/>
    <line x1="340" y1="121" x2="385" y2="121" stroke="var(--blue)" stroke-width="5"/>
    <circle cx="84" cy="121" r="21" fill="#fff"/>
    <path d="M88 113l-8 8 8 8" fill="none" stroke="#222" stroke-width="2.5"/>
    <circle cx="1114" cy="121" r="21" fill="#fff"/>
    <path d="M1110 113l8 8-8 8" fill="none" stroke="#222" stroke-width="2.5"/>
    <g stroke="var(--navy)" stroke-width="4">
      <circle cx="245" cy="121" r="97" fill="#2c3f55"/>
      <circle cx="718" cy="121" r="97" fill="#9aa7b2"/>
      <circle cx="957" cy="121" r="97" fill="#c5ccd3"/>
    </g>
    <circle cx="482" cy="121" r="97" fill="#3f7c9a" stroke="var(--blue)" stroke-width="6"/>
  </svg>
  <div class="abs" role="img" aria-label="Project photos: X-ray scans, surgical team, ultrasound unit, radiotherapy machine" style="left:0;top:0;width:0;height:0"></div>
  <div class="year" style="left:185px">2019</div>
  <div class="year" style="left:422px">2020</div>
  <div class="year" style="left:658px">2021</div>
  <div class="year" style="left:897px">2022</div>

  <div class="abs" style="left:112px;top:532px;font-size:21px">2020 Projects</div>
  <div class="abs" style="left:112px;top:579px;width:498px;height:3px;background:#5a5f7e"></div>
  <div class="month" style="top:616px">January</div>
  <div class="month-text" style="top:656px">Nemo enim ipsam voluptatem quia voluptas sit aspernatur aut odit aut fugit, sed quia consequuntur magni.</div>
  <div class="month" style="top:736px">March</div>
  <div class="month-text" style="top:776px">Nemo enim ipsam voluptatem quia voluptas sit aspernatur aut odit aut fugit, sed quia consequuntur magni.</div>
  <div class="month" style="top:856px">August</div>
  <div class="month-text" style="top:896px">Nemo enim ipsam voluptatem quia voluptas sit aspernatur aut odit aut fugit, sed quia consequuntur magni.</div>

  <div class="photo" role="img" aria-label="Surgical team operating under theatre lights" style="left:695px;top:551px;width:307px;height:370px;background:linear-gradient(160deg,#4b6a86 0%,#2f6a8c 45%,#6fb2cf 75%,#2d4f68 100%)"></div>
</section>

<section class="services">
  <div class="abs label center" style="top:87px">WHAT WE DO</div>
  <div class="abs heading center" style="top:126px">Services We Provide</div>
  <div class="card" role="img" aria-label="Two businessmen discussing sales at a laptop" style="left:112px;width:307px;background:linear-gradient(180deg,#7d7a73 0%,#5c5a6a 50%,#24225f 100%)"><div class="card-title">Sales</div></div>
  <div class="card" role="img" aria-label="Hand operating an ultrasound machine control panel" style="left:445px;width:309px;background:linear-gradient(180deg,#3b5e86 0%,#6f93b5 45%,#4aa8de 100%)"><div class="card-title">Distribution</div></div>
  <div class="card" role="img" aria-label="Technician servicing a surgical microscope" style="left:779px;width:309px;background:linear-gradient(180deg,#c9ced3 0%,#8b93a0 45%,#2a2b66 100%)"><div class="card-title">Services</div></div>
</section>

<section class="training">
  <div class="photo" role="img" aria-label="Nurses training on a medical device screen" style="left:0;top:0;width:637px;height:548px;background:linear-gradient(135deg,#b9a99a 0%,#e2e4e7 40%,#9eb2c8 70%,#f0f2f4 100%)"></div>
  <div class="abs label" style="left:695px;top:74px">SUPPORT</div>
  <div class="abs heading" style="left:695px;top:114px">Training</div>
  <div class="abs body-text" style="left:695px;top:197px;width:400px">Sed ut perspiciatis unde omnis iste natus error sit voluptatem accusantium doloremque laudantium, totam rem aperiam, eaque ipsa quae ab illo inven tore veritatis et quasi architecto beatae vitae dicta sunt explicabo. Nemo enim ipsam voluptatem quia voluptas sit aspernatur aut odit.</div>
  <div class="btn" style="left:695px;top:402px;width:157px;height:61px">READ MORE</div>
</section>

<section class="partners">
  <div class="abs label center" style="top:86px">FEATURED COMPANIES</div>
  <div class="abs heading center" style="top:126px">Our Partners</div>
  <svg class="abs" style="left:66px;top:260px" width="16" height="26" viewBox="0 0 16 26"><path d="M12 3L3 13l9 10" fill="none" stroke="#333" stroke-width="2.5"/></svg>
  <svg class="abs" style="left:1110px;top:260px" width="16" height="26" viewBox="0 0 16 26"><path d="M4 3l9 10-9 10" fill="none" stroke="#333" stroke-width="2.5"/></svg>
  <div class="partner" style="left:112px"><i></i></div>
  <div class="partner" style="left:311px"><i style="border-radius:50%"></i></div>
  <div class="partner active" style="left:509px"><i style="background:#d9a9a0"></i></div>
  <div class="partner" style="left:706px"><i></i></div>
  <div class="partner" style="left:906px"><i style="border-radius:50%"></i></div>
</section>

<footer class="site-footer">
  <div class="abs brand" style="left:112px;top:68px">
    <div class="brand-mark" style="background:#fff;width:50px;height:50px"></div>
    <div>
      <div class="brand-name" style="color:#fff;font-size:34px">BenQoral Medical</div>
      <div class="brand-sub" style="color:#fff;font-size:11px;letter-spacing:3px">FOR MEDICAL APPLIANCES</div>
    </div>
  </div>
  <div class="abs" style="left:112px;top:184px;width:430px;font-size:16px;line-height:27px">We are a medical supplier company we sell machines and equipment to all medical sectors in Iraq.</div>

  <div class="abs footer-title" style="left:605px;top:62px">Quick Links</div>
  <div class="abs footer-links" style="left:605px;top:107px">Home<br>Projects<br>Services<br>Training<br>About<br>Contact us</div>

  <div class="abs footer-title" style="left:821px;top:62px">Contact Information</div>
  <svg class="abs" style="left:821px;top:113px" width="12" height="16" viewBox="0 0 12 16"><path d="M6 0a6 6 0 0 1 6 6c0 4-6 10-6 10S0 10 0 6a6 6 0 0 1 6-6z" fill="#fff"/><circle cx="6" cy="6" r="2.2" fill="var(--navy-deep)"/></svg>
  <div class="abs footer-contact" style="left:845px;top:109px">Lorem ipsum Street,<br>1234 Building-3rd Floor</div>
  <svg class="abs" style="left:821px;top:166px" width="15" height="15" viewBox="0 0 24 24"><path fill="#fff" d="M6.6 10.8a15 15 0 0 0 6.6 6.6l2.2-2.2c.3-.3.7-.4 1-.2 1.1.4 2.3.6 3.6.6.6 0 1 .4 1 1V20c0 .6-.4 1-1 1A17 17 0 0 1 3 4c0-.6.4-1 1-1h3.5c.6 0 1 .4 1 1 0 1.3.2 2.5.6 3.6.1.3 0 .7-.2 1z"/></svg>
  <div class="abs footer-contact" style="left:849px;top:161px">1 800 555 0142</div>
  <svg class="abs" style="left:821px;top:223px" width="17" height="13" viewBox="0 0 17 13"><rect width="17" height="13" rx="1" fill="#fff"/><path d="M1 1l7.5 6L16 1" fill="none" stroke="var(--navy-deep)" stroke-width="1.5"/></svg>
  <div class="abs footer-contact" style="left:853px;top:217px">info@benqoral.example</div>

  <div class="abs" style="left:112px;top:316px;width:976px;height:1px;background:#3b3f86"></div>
  <div class="abs" style="left:112px;top:348px;font-size:16px">Copyright © 2024, BenQoral Medical. All rights reserved. Privacy Policy &nbsp;|&nbsp; Terms of Service.</div>
  <div class="social" style="left:875px"></div>
  <div class="social" style="left:931px"></div>
  <div class="social" style="left:987px"></div>
  <div class="social" style="left:1043px"></div>
</footer>

</body>
</html>
```